Business Card Design

Marla Quibbet
Artist of Contemporary/Modern/Representational Art
Contact: 0457219308
Please include my web site (thanks)! http://www.artvault913.com.au/marla-quibbet
And
Email: marlaquibbet@fernpost.example

Target Market(s)

Modern professional People who know what they like in modern contemporary art and have the means to purchase it.

Industry/Entity Type

Business

Contact Information for Business Card

Marla Quibbet
Contact: 0457219308

Font styles to use
Sans Serif

Requirements
Must have
• Simplicity & to the point
Keep the font modern/ contemporary
Nice to have
• A portrait of me and one piece of work on the business card (one on each side).
Should not have
• I'm not into butterflies.
No feminine style swirls
Nor I like swirls that look like tatoos

```html
<!DOCTYPE html>
<html lang="en">
<head>
<meta charset="utf-8">
<title>Marla Quibbet – Business Card</title>
<link rel="stylesheet" href="https://fonts.googleapis.com/css2?family=Bungee&family=Kreon:wght@700&display=swap">
<style>
  :root {
    --page: #ffffff;
    --card: #f9f8f9;
    --navy: #1c2a5c;
    --sky-deep: #21496f;
    --sky: #4f86a8;
    --red: #c8432a;
    --green: #9cae58;
    --yellow: #e6d23c;
    --ground: #6e4a3a;
    --ground-light: #b89c8e;
  }
  * { margin: 0; padding: 0; box-sizing: border-box; }
  html, body {
    width: 927px;
    height: 1200px;
    overflow: hidden;
    background: var(--page);
  }
  .sheet {
    position: relative;
    width: 927px;
    height: 1200px;
  }
  .card-front {
    position: absolute;
    left: 50px;
    top: 66px;
    width: 830px;
    height: 494px;
    background: var(--card);
  }
  .name {
    position: absolute;
    left: 0;
    right: 0;
    top: 150px;
    text-align: center;
    font-family: "Bungee", sans-serif;
    font-size: 56px;
    line-height: 1;
    color: var(--navy);
    letter-spacing: 1px;
  }
  .tagline {
    position: absolute;
    left: 0;
    right: 0;
    top: 226px;
    text-align: center;
    font-family: "Kreon", serif;
    font-weight: 700;
    font-size: 21px;
    color: var(--navy);
  }
  .contact {
    position: absolute;
    right: 52px;
    top: 370px;
    text-align: right;
    font-family: "Kreon", serif;
    font-weight: 700;
    font-size: 22px;
    line-height: 33px;
    color: var(--navy);
  }
  .card-back {
    position: absolute;
    left: 50px;
    top: 600px;
    width: 811px;
    height: 483px;
    overflow: hidden;
  }
  .artwork {
    position: absolute;
    inset: 0;
    background:
      linear-gradient(90deg, rgba(200,67,42,0.55) 0%, rgba(156,174,88,0.35) 22%, rgba(200,67,42,0.5) 36%, rgba(230,210,60,0.55) 58%, rgba(156,174,88,0.45) 76%, rgba(200,67,42,0.5) 100%),
      linear-gradient(180deg, var(--sky-deep) 0%, var(--sky) 12%, var(--green) 22%, var(--red) 45%, var(--yellow) 60%, var(--ground) 72%, var(--ground-light) 86%, var(--ground) 100%);
  }
  .artwork-name {
    position: absolute;
    left: 0;
    right: 0;
    top: 212px;
    text-align: center;
    font-family: "Bungee", sans-serif;
    font-size: 62px;
    line-height: 1;
    color: var(--navy);
  }
</style>
</head>
<body>
<main class="sheet">
  <section class="card-front">
    <h1 class="name">Marla Quibbet</h1>
    <p class="tagline">Artist of Contemporary/Modern/Representational Art</p>
    <p class="contact">Contact: 0457219308<br>www.artvault913.com.au/marla-quibbet</p>
  </section>
  <section class="card-back">
    <div class="artwork" role="img" aria-label="Painting of a row of colourful leaning townhouses under a blue sky above a reflective waterfront with blossoming trees"></div>
    <p class="artwork-name">Marla Quibbet</p>
  </section>
</main>
</body>
</html>
```